Quorvant Group Invitation

I need an invitation designed for both online and hard copy distribution. I'm uploading a poorly designed online invitation that includes our logo and the blue and black colors we want to use. The online invitation must have an area to embed video (see attached).

With regard to the hard copy invitation, we need it to be a 5x7 card. Where the embedded video is on the online version, we would like you to create an image that represents the terms "monetizing innovation". If you go to www.qvgroup.co, you can see what the company is using to express those words right now. There are no limitations to what you come up with for this visual.

Please note: The invitation both online and hardcopy must be designed so that all the information in the attached copy can be read. This includes: Logo, hosted by; When/date, where, two quotes, etc.

I've attached our logo files. You can use whichever logo file you want for your design.

Many thanks...looking forward to seeing all your great designs.
Updates

All - you do not need to follow our format for the invite as long as all the information we need is on it....Note:  we will need to be able to edit the information for other presentation.

EPS files of the logo have been added for those of you who have requested it.

Many thanks,

Marla

Reason: All, Apologies for the extension. The decision-makers have been travelling and have not had a chance to thoroughly review the designs. We really appreciate your patience. Many thanks, Marla

Target Market(s)

Investors and Media

Industry/Entity Type

It Company

Requirements
Must have
• Please use the blue and black colors as seen in the attached uploaded files.

```html
<!DOCTYPE html>
<html lang="en">
<head>
<meta charset="utf-8">
<title>Quorvant Group – Monetizing Innovation Invitation</title>
<link href="https://fonts.googleapis.com/css2?family=Arimo:wght@400;700&display=swap" rel="stylesheet">
<style>
  :root {
    --page: #ececec;
    --card: #ffffff;
    --blue: #1f74bb;
    --blue-band: #2a7fc1;
    --ink: #111111;
    --white: #ffffff;
    --rule-blue: #2f86c8;
  }
  * { margin: 0; padding: 0; box-sizing: border-box; }
  html, body { width: 1200px; height: 978px; overflow: hidden; }
  body {
    background: var(--page);
    font-family: "Arimo", Arial, sans-serif;
    color: var(--ink);
    position: relative;
  }
  .invite {
    position: absolute;
    top: 25px;
    height: 928px;
    background: linear-gradient(180deg, #ffffff 0%, #f6f9fc 60%, #ffffff 100%);
    overflow: hidden;
  }
  .invite--print { left: 17px; width: 677px; }
  .invite--online { left: 722px; width: 464px; }
  .abs { position: absolute; }

  .kicker { color: var(--blue); font-weight: 700; text-transform: uppercase; }
  .brand { display: flex; align-items: center; gap: 12px; }
  .brand__mark { width: 26px; height: 26px; background: var(--blue); }
  .brand__name { color: var(--blue); font-weight: 700; letter-spacing: 3px; text-transform: uppercase; }

  .headline { color: var(--blue); font-weight: 700; text-transform: uppercase; text-align: center; }
  .bullets { list-style: none; font-weight: 700; color: var(--ink); }
  .bullets li::before { content: "\2022\00a0"; }

  .detail-label { color: var(--ink); font-weight: 700; }
  .detail-value { color: var(--blue); font-weight: 700; }
  .hosts { font-weight: 700; color: var(--blue); text-transform: uppercase; }
  .hosts b { color: var(--ink); }

  .rule { left: 0; right: 0; background: var(--rule-blue); }
  .rsvp {
    left: 0; right: 0; bottom: 0;
    background: var(--blue-band);
    color: var(--white);
    text-align: center;
    font-weight: 700;
  }
  .rsvp__title { text-transform: uppercase; }
  .rsvp__contact { text-transform: uppercase; }
  .rsvp__url { }
  .rsvp__note { color: var(--ink); font-weight: 700; }
</style>
</head>
<body>

<!-- Print invitation (5x7) -->
<section class="invite invite--print">
  <p class="abs kicker" style="top:40px;left:0;right:0;text-align:center;font-size:15px;">A Special Presentation of</p>
  <div class="abs brand" style="top:190px;left:0;right:0;justify-content:center;">
    <span class="brand__mark"></span>
    <span class="brand__name" style="font-size:24px;">Quorvant Group</span>
  </div>

  <h1 class="abs headline" style="top:268px;left:0;right:0;font-size:25px;">Monetizing Innovation</h1>

  <ul class="abs bullets" style="top:308px;left:40px;right:20px;font-size:21px;line-height:25px;">
    <li>In the biggest breakthrough against malaria in years, scientist yesterday said they had identifiedthe odor molecules that baffle blood-thirsty mosquitoes.</li>
    <li style="margin-top:22px;">Confusing mosquitoes to fight deadly disease.</li>
  </ul>

  <div class="abs" style="top:462px;left:53px;font-size:17px;line-height:18px;">
    <p class="detail-label">WHEN:</p>
    <p class="detail-value">Wednesday, September 28th<br>Check-In 3:00 pm<br>Presentation 3:30 - 4:30 pm</p>
  </div>
  <div class="abs" style="top:462px;left:352px;font-size:17px;line-height:18px;">
    <p class="detail-label">WHERE:</p>
    <p class="detail-value">Harbor Crest Inn – Laguna Room<br>2150 Crestview Ave<br>Lakemont CA 92580</p>
  </div>

  <p class="abs hosts" style="top:548px;left:28px;right:10px;font-size:17px;line-height:18px;">
    <b>HOSTED BY:</b> Tarek Mansouri, CEO, Glen Whitaker, President<br>Ray Delgado, CFO, Mark Ellison, COO, Evan Pryce, CCO
  </p>

  <div class="abs rule" style="top:594px;height:9px;"></div>

  <div class="abs" role="img" aria-label="Photo of a thoughtful woman with idea sketches" style="top:614px;left:0;width:159px;height:151px;background:linear-gradient(135deg,#d9d2c6,#8a7a68);"></div>
  <div class="abs" role="img" aria-label="Photo of a business team meeting at a table" style="top:614px;left:163px;width:183px;height:151px;background:linear-gradient(135deg,#f1f1f1,#b9bcc0);"></div>
  <div class="abs" role="img" aria-label="Photo of business silhouettes against a bright window" style="top:614px;left:352px;width:181px;height:151px;background:linear-gradient(180deg,#cfd9e3,#33404d);"></div>
  <div class="abs" role="img" aria-label="Photo of financial charts and a calculator" style="top:614px;left:539px;width:138px;height:151px;background:linear-gradient(135deg,#9fb3c6,#3d5670);"></div>

  <footer class="abs rsvp" style="height:151px;padding-top:10px;">
    <p class="rsvp__title" style="font-size:17px;line-height:18px;">Please RSVP by Monday,</p>
    <p class="rsvp__contact" style="font-size:13px;line-height:14px;">Nora Valdez, Date : September 26th<br>Number : (877) 555-0148 x1003, Email : nvaldez@qvgroup.co</p>
    <p class="rsvp__url" style="font-size:22px;margin-top:10px;">www.qvgroup.co</p>
    <p class="rsvp__note" style="font-size:10px;margin-top:12px;">*Please note that you must be an accredited investor to attend the presentation</p>
  </footer>
</section>

<!-- Online invitation -->
<section class="invite invite--online">
  <p class="abs kicker" style="top:30px;left:174px;font-size:13px;">A Special Presentation of</p>
  <div class="abs brand" style="top:72px;left:90px;">
    <span class="brand__mark"></span>
    <span class="brand__name" style="font-size:19px;">Quorvant Group</span>
  </div>

  <div class="abs" style="top:165px;left:28px;font-size:12.5px;line-height:13px;">
    <p class="detail-label">WHEN:</p>
    <p class="detail-value">Wednesday, September 28th<br>Check-In 3:00 pm<br>Presentation 3:30 - 4:30 pm</p>
  </div>
  <div class="abs" style="top:165px;left:237px;font-size:12.5px;line-height:13px;">
    <p class="detail-label">WHERE:</p>
    <p class="detail-value">Harbor Crest Inn – Laguna Room<br>2150 Crestview Ave<br>Lakemont CA 92580</p>
  </div>

  <p class="abs hosts" style="top:225px;left:14px;right:6px;font-size:12.5px;line-height:14px;">
    <b>HOSTED BY:</b> Tarek Mansouri, CEO, Glen Whitaker, President<br>Ray Delgado, CFO, Mark Ellison, COO, Evan Pryce, CCO
  </p>

  <ul class="abs bullets" style="top:268px;left:12px;right:12px;font-size:17px;line-height:24px;">
    <li>In the biggest breakthrough against malaria in years, scientist yesterday said they had identifiedthe odor molecules that baffle blood-thirsty mosquitoes.</li>
    <li style="margin-top:20px;">Confusing mosquitoes to fight deadly disease.</li>
  </ul>

  <div class="abs rule" style="top:418px;height:12px;"></div>

  <div class="abs" role="img" aria-label="Embedded news video still" style="top:453px;left:34px;width:398px;height:298px;background:#111;padding:12px 6px;">
    <div style="width:100%;height:100%;background:radial-gradient(ellipse at 40% 40%,#c9d6ef 0%,#4a5fb0 35%,#1d2a6a 70%,#0b1230 100%);"></div>
  </div>

  <h2 class="abs headline" style="top:765px;left:0;right:0;font-size:28px;">Monetizing Innovation</h2>

  <footer class="abs rsvp" style="height:121px;padding-top:12px;">
    <p class="rsvp__title" style="font-size:15px;line-height:16px;">Please RSVP by Monday,</p>
    <p class="rsvp__contact" style="font-size:11.5px;line-height:13px;">Nora Valdez, Date : September 26th<br>Number : (877) 555-0148 x1003, Email : nvaldez@qvgroup.co</p>
    <p class="rsvp__url" style="font-size:20px;margin-top:6px;">www.qvgroup.co</p>
    <p class="rsvp__note" style="font-size:9.5px;margin-top:8px;">*Please note that you must be an accredited investor to attend the presentation</p>
  </footer>
</section>

</body>
</html>
```